Dining hall menu app needs a redesign

We are looking for a redesign of our app TrayPlate which is available for iOS for free on the Kestrel AppHub.

The app allows students of most of Germany's universities to show the menu of their university's dining hall. Currently there are about 400 dining halls to view the menu of. A menu contains the a list of meals for the next couple of days (usually for the next 5-7 days). Each meal can be rated by the users and photos can be uploaded. The following data should be visible for each meal in the meal list:
- The date the meal is available
- The meal category (usually a short text, categorizing the meal)
- Name of the meal (can be very long but it's ok to truncate it after the second line)
- Average meal rating (5-star rating)
- A photo of the meal
- Up to 4 prices (e.g. usually students pay less than employees, which is why multiple prices for the same meal are available. In the menu list only the prices are shown)

When selecting a meal, more details about the meal are shown:
- Full meal name
- Up to 4 prices including the price type (e.g. Student: 3.40€, Employees: 4.20€)
- Total number of ratings
- Total number of comments
- A list of additives and info-texts about the meal (e.g. whether the meal is vegetarian, or contains food additives)
- A list of photos including a relative date when the photo has been taken (e.g. "2 months ago")

Additionally a user should be able to add a review to the meal (5 star rating and an optional comment), view the list of comments, take a photo of the meal and to share it on chatterbook/blipster/via email.

All views show an advertisement banner on the bottom of the view.

The design should be very modern and clean. We don't like a skeuomorphic design. The content of the app is most important. Other than that you are free to design something pretty.
Updates

Target Market(s)

Students (age between 19 and 30)

Industry/Entity Type

University

Requirements
Must have
• At least we need a redesign of the meal list, the meal detail page, the app-logo and the splashscreen.
Nice to have
• Design for the meal review page, the dining hall list and the favorites list.
Should not have
• No skeuomorphic design and not too many colors.

```html
<!DOCTYPE html>
<html lang="en">
<head>
<meta charset="utf-8">
<title>TrayPlate – meal detail and dining hall list</title>
<link href="https://fonts.googleapis.com/css2?family=Arimo:wght@400;700&family=Cookie&display=swap" rel="stylesheet">
<style>
:root{
  --stage:#1b1c1f;
  --blue:#2f6fcb;
  --blue-light:#3b7fd8;
  --blue-line:#5a95e0;
  --link:#2a6fd0;
  --ink:#4a4a4a;
  --ink-soft:#6e6e6e;
  --row:#e3e3e3;
  --row-alt:#e9e9e9;
  --section:#cfcfcf;
  --rule:#c4c4c4;
  --dark:#2c2c2c;
  --status:#000;
  --gold:#f3b31a;
  --star-off:#202020;
  --star-light:#c9c9c9;
  --tab:#2d2d2d;
  --tab-active:#1f1f1f;
  --tab-text:#cfcfcf;
  --fav-box:#d9d9d9;
  --fav-off:#ededed;
}
*{box-sizing:border-box;margin:0;padding:0}
html,body{width:1200px;height:849px;overflow:hidden;background:var(--stage)}
body{font-family:"Arimo",Arial,sans-serif}
.stage{position:relative;width:1169px;height:827px;transform:scale(1.0265);transform-origin:0 0}
.screen{position:absolute;top:70px;width:467px;height:702px;background:var(--row);overflow:hidden}
.screen--detail{left:66px}
.screen--list{left:635px}

.status-bar{height:30px;background:var(--status);color:#fff;display:flex;align-items:center;padding:0 8px;font-weight:700;font-size:17px;position:relative}
.status-bar .signal{display:flex;align-items:flex-end;gap:2px;margin-right:6px;height:12px}
.status-bar .signal i{display:block;width:3px;background:#fff}
.status-bar .net{margin-left:12px}
.status-bar .lock{position:absolute;left:50%;transform:translateX(-50%);top:6px}
.status-bar .battery{position:absolute;right:8px;top:9px;width:28px;height:13px;border:2px solid #fff;border-radius:2px;padding:1px}
.status-bar .battery::after{content:"";position:absolute;right:-5px;top:2px;width:3px;height:5px;background:#fff}
.status-bar .battery i{display:block;height:100%;background:#fff}

.app-header{height:62px;background:linear-gradient(var(--blue-light),var(--blue));position:relative;border-bottom:3px solid #1f4f96}
.app-header .title{position:absolute;left:0;right:0;top:4px;text-align:center;font-family:"Cookie",cursive;font-weight:400;font-size:48px;color:#e8f0fb;line-height:52px}
.app-header .btn{position:absolute;top:0;height:62px;display:flex;align-items:center;justify-content:center}
.app-header .btn.left{left:0;width:71px;border-right:1px solid #255ea9}
.app-header .btn.r1{right:67px;width:66px;border-left:1px solid #255ea9}
.app-header .btn.r2{right:0;width:67px;border-left:1px solid #255ea9}
.screen--list .app-header .btn.r2{width:71px}

.gallery{height:210px;background:var(--dark);position:relative;border-top:4px solid #d5d5d5}
.gallery .shot{position:absolute;top:10px;width:180px;height:184px;border:2px solid #e6e6e6;border-radius:5px;overflow:hidden}
.gallery .shot .fill{width:100%;height:100%}
.gallery .shot .date{position:absolute;top:8px;left:0;right:0;text-align:center;color:#fff;font-size:16px}
.shot--pasta{left:-14px}.shot--pasta .fill{background:radial-gradient(circle at 45% 55%,#d4893c,#a6401f 55%,#3a2a22)}
.shot--pancake{left:190px;width:206px}.shot--pancake .fill{background:radial-gradient(circle at 50% 55%,#efce5a,#c99a3d 45%,#6f8ba0 75%,#3f4f5e)}
.shot--salad{left:405px;width:100px}.shot--salad .fill{background:radial-gradient(circle at 40% 60%,#c98a4a,#5c7a33 55%,#2b3325)}

.ratings-bar{height:42px;background:#333;border-top:4px solid #c9c9c9;display:flex;align-items:center;justify-content:space-between;padding:0 10px 0 8px;color:#fff;font-weight:700;font-size:18px}
.stars{display:flex;gap:1px}
.description{padding:5px 24px 0 10px;height:94px;font-size:18.5px;line-height:30px;color:var(--ink-soft);background:var(--row-alt)}
.price-row{height:46px;display:flex;align-items:center;justify-content:space-between;padding:0 14px;border-top:1px solid var(--rule);background:var(--row);font-size:19px}
.price-row .type{font-weight:700;color:var(--ink)}
.price-row .amount{color:var(--link)}
.section-head{height:36px;background:var(--section);padding:0 14px;display:flex;align-items:center;font-weight:700;font-size:19px;color:var(--ink)}
.rate-row{height:61px;display:flex;align-items:center;justify-content:center;gap:5px;background:var(--row-alt);border-bottom:1px solid var(--rule)}
.comment-row{height:48px;display:flex;align-items:center;justify-content:space-between;padding:0 14px;color:var(--link);font-weight:700;font-size:19px;background:var(--row)}

.hall-list{height:536px;overflow:hidden;background:var(--row)}
.hall{height:114.5px;position:relative;border-top:1px solid var(--rule);padding:12px 14px 0;background:linear-gradient(var(--row-alt),var(--row))}
.hall:first-child{border-top:none}
.hall .name{font-weight:700;font-size:25px;color:var(--ink);line-height:30px}
.hall .distance{display:flex;align-items:center;gap:6px;font-weight:700;font-size:19px;line-height:22px;color:var(--ink-soft);margin-top:8px}
.hall .address{color:var(--link);font-size:19px;line-height:22px;margin-top:6px}
.hall .fav{position:absolute;right:15px;top:30px;width:59px;height:59px;background:var(--fav-box);border-radius:3px;display:flex;align-items:center;justify-content:center}

.tab-bar{position:absolute;left:0;right:0;bottom:0;height:68px;background:var(--tab);display:flex}
.tab{flex:1;display:flex;flex-direction:column;align-items:center;justify-content:flex-end;padding-bottom:3px;gap:4px;color:var(--tab-text);font-size:16px;border-left:1px solid #3b3b3b}
.tab:first-child{border-left:none}
.tab.active{background:var(--tab-active);color:#d9d9d9}
</style>
</head>
<body>
<svg width="0" height="0" style="position:absolute">
  <defs>
    <symbol id="star" viewBox="0 0 24 24"><path d="M12 1.5l3.2 7 7.5.7-5.7 5 1.7 7.4L12 17.7 5.3 21.6 7 14.2 1.3 9.2l7.5-.7z"/></symbol>
    <symbol id="heart" viewBox="0 0 24 24"><path d="M12 21.5C5 16 1.5 12.5 1.5 8A5.5 5.5 0 0 1 12 5.3 5.5 5.5 0 0 1 22.5 8c0 4.5-3.5 8-10.5 13.5z"/></symbol>
    <symbol id="pin" viewBox="0 0 24 24"><path d="M12 1a8 8 0 0 0-8 8c0 6 8 14 8 14s8-8 8-14a8 8 0 0 0-8-8zm0 11a3 3 0 1 1 0-6 3 3 0 0 1 0 6z"/></symbol>
  </defs>
</svg>

<div class="stage">

  <section class="screen screen--detail" aria-label="Meal detail">
    <div class="status-bar">
      <span class="signal"><i style="height:3px"></i><i style="height:5px"></i><i style="height:7px"></i><i style="height:9px"></i><i style="height:12px"></i></span>
      VELTRA<span class="net">3G</span>
      <svg class="lock" width="14" height="18" viewBox="0 0 14 18"><rect x="1" y="8" width="12" height="10" rx="1" fill="#fff"/><path d="M3.5 8V5a3.5 3.5 0 0 1 7 0v3" stroke="#fff" stroke-width="2" fill="none"/></svg>
      <span class="battery"><i></i></span>
    </div>
    <header class="app-header">
      <span class="btn left"><svg width="38" height="38" viewBox="0 0 38 38" fill="none" stroke="#fff" stroke-width="2.5"><circle cx="19" cy="19" r="17"/><path d="M27 19H11M17 12l-7 7 7 7"/></svg></span>
      <h1 class="title">info</h1>
      <span class="btn r1"><svg width="38" height="38" viewBox="0 0 38 38" fill="none" stroke="#fff" stroke-width="2.5"><circle cx="19" cy="19" r="17"/><path d="M12 25c1-6 5-9 12-9" /><path d="M20 11l6 5-6 5" fill="#fff"/></svg></span>
      <span class="btn r2"><svg width="38" height="38" viewBox="0 0 38 38" fill="none" stroke="#fff" stroke-width="2.5"><circle cx="19" cy="19" r="17"/><rect x="11" y="14" width="16" height="11" rx="2" fill="#fff" stroke="none"/><rect x="15" y="12" width="8" height="3" fill="#fff" stroke="none"/><circle cx="19" cy="19.5" r="3" fill="var(--blue)" stroke="none"/></svg></span>
    </header>

    <div class="gallery">
      <figure class="shot shot--pasta"><div class="fill" role="img" aria-label="Photo of spaghetti with tomato sauce and parmesan"></div><span class="date">May 25, 2011</span></figure>
      <figure class="shot shot--pancake"><div class="fill" role="img" aria-label="Photo of pancakes with cream and a strawberry"></div><span class="date">May 25, 2011</span></figure>
      <figure class="shot shot--salad"><div class="fill" role="img" aria-label="Photo of a pasta salad with vegetables"></div><span class="date">May 25, 2011</span></figure>
    </div>

    <div class="ratings-bar">
      <span>(5 ratings)</span>
      <span class="stars">
        <svg width="22" height="22" fill="var(--gold)"><use href="#star"/></svg>
        <svg width="22" height="22" fill="var(--gold)"><use href="#star"/></svg>
        <svg width="22" height="22" fill="var(--gold)"><use href="#star"/></svg>
        <svg width="22" height="22" fill="var(--star-off)"><use href="#star"/></svg>
        <svg width="22" height="22" fill="var(--star-off)"><use href="#star"/></svg>
      </span>
    </div>

    <p class="description">Lorem Ipsum proin gravida nibh vel velit auctor ali-quet. Aenean sollicitudin, lorem quis bibendum auctor, nisi elit consequat ipsum.</p>

    <div class="price-row"><span class="type">Student</span><span class="amount">€3.90</span></div>
    <div class="price-row"><span class="type">Gast</span><span class="amount">€4.90</span></div>
    <div class="section-head">Rating</div>
    <div class="rate-row">
      <svg width="37" height="37" fill="var(--star-light)"><use href="#star"/></svg>
      <svg width="37" height="37" fill="var(--star-light)"><use href="#star"/></svg>
      <svg width="37" height="37" fill="var(--star-light)"><use href="#star"/></svg>
      <svg width="37" height="37" fill="var(--star-light)"><use href="#star"/></svg>
      <svg width="37" height="37" fill="var(--star-light)"><use href="#star"/></svg>
    </div>
    <div class="comment-row"><span>2 Comment</span><svg width="12" height="18" viewBox="0 0 12 18" fill="none" stroke="var(--link)" stroke-width="3"><path d="M2 2l7 7-7 7"/></svg></div>
    <div class="section-head">Additives</div>
  </section>

  <section class="screen screen--list" aria-label="Dining hall list">
    <div class="status-bar">
      <span class="signal"><i style="height:3px"></i><i style="height:5px"></i><i style="height:7px"></i><i style="height:9px"></i><i style="height:12px"></i></span>
      VELTRA<span class="net">3G</span>
      <svg class="lock" width="14" height="18" viewBox="0 0 14 18"><rect x="1" y="8" width="12" height="10" rx="1" fill="#fff"/><path d="M3.5 8V5a3.5 3.5 0 0 1 7 0v3" stroke="#fff" stroke-width="2" fill="none"/></svg>
      <span class="battery"><i></i></span>
    </div>
    <header class="app-header">
      <h1 class="title">label</h1>
      <span class="btn r2"><svg width="38" height="38" viewBox="0 0 38 38" fill="none" stroke="#fff" stroke-width="2.5"><circle cx="19" cy="19" r="17"/><path d="M11 17a8 8 0 0 1 15-3M27 21a8 8 0 0 1-15 3"/><path d="M27 9v6h-6M11 29v-6h6"/></svg></span>
    </header>

    <div class="hall-list">
      <article class="hall">
        <h2 class="name">Nordtal-Westmark</h2>
        <p class="distance"><svg width="16" height="20" fill="var(--ink-soft)"><use href="#pin"/></svg>Deistance : 185 km</p>
        <p class="address">Lindenweg 12, 70199 Falkheim</p>
        <span class="fav"><svg width="34" height="34" fill="var(--blue)"><use href="#heart"/></svg></span>
      </article>
      <article class="hall">
        <h2 class="name">Nordtal-Westmark</h2>
        <p class="distance"><svg width="16" height="20" fill="var(--ink-soft)"><use href="#pin"/></svg>Deistance : 185 km</p>
        <p class="address">Lindenweg 12, 70199 Falkheim</p>
        <span class="fav"><svg width="34" height="34" fill="var(--fav-off)"><use href="#heart"/></svg></span>
      </article>
      <article class="hall">
        <h2 class="name">Nordtal-Westmark</h2>
        <p class="distance"><svg width="16" height="20" fill="var(--ink-soft)"><use href="#pin"/></svg>Deistance : 185 km</p>
        <p class="address">Lindenweg 12, 70199 Falkheim</p>
        <span class="fav"><svg width="34" height="34" fill="var(--blue)"><use href="#heart"/></svg></span>
      </article>
      <article class="hall">
        <h2 class="name">Nordtal-Westmark</h2>
        <p class="distance"><svg width="16" height="20" fill="var(--ink-soft)"><use href="#pin"/></svg>Deistance : 185 km</p>
        <p class="address">Lindenweg 12, 70199 Falkheim</p>
        <span class="fav"><svg width="34" height="34" fill="var(--fav-off)"><use href="#heart"/></svg></span>
      </article>
      <article class="hall">
        <h2 class="name">Nordtal-Westmark</h2>
        <p class="distance"><svg width="16" height="20" fill="var(--ink-soft)"><use href="#pin"/></svg>Deistance : 185 km</p>
        <p class="address">Lindenweg 12, 70199 Falkheim</p>
        <span class="fav"><svg width="34" height="34" fill="var(--fav-off)"><use href="#heart"/></svg></span>
      </article>
    </div>

    <nav class="tab-bar">
      <span class="tab active"><svg width="40" height="34" viewBox="0 0 40 34" fill="none" stroke="var(--blue-line)" stroke-width="3" stroke-linecap="round"><path d="M8 3v8a4 4 0 0 0 8 0V3M12 3v30M30 3c-5 3-5 12 0 14v16M8 31L30 5"/></svg>Canteens</span>
      <span class="tab"><svg width="24" height="32" fill="#cfcfcf"><use href="#pin"/></svg>Map</span>
      <span class="tab"><svg width="34" height="32" fill="#cfcfcf"><use href="#heart"/></svg>Favorites</span>
    </nav>
  </section>

</div>
</body>
</html>
```